Working Capital graphics

Our business advisory firm requires 9 images to be re-created and improved in the branding of our business.

The 9 images have been uploaded below and the colours and branding of the business can be found at the website www.thornwickadvisory.com.au

```html
<!DOCTYPE html>
<html lang="en">
<head>
<meta charset="utf-8">
<title>Receivables Drivers</title>
<link href="https://fonts.googleapis.com/css2?family=Noto+Serif:ital,wght@0,400;0,600;1,400;1,600;1,700&display=swap" rel="stylesheet">
<style>
  :root {
    --brand-orange: #f59322;
    --brand-maroon: #851820;
    --paper: #ffffff;
    --ink: #111111;
  }
  * { box-sizing: border-box; margin: 0; padding: 0; }
  html, body { width: 1200px; height: 1000px; overflow: hidden; background: var(--paper); }
  .canvas { position: relative; width: 1200px; height: 1000px; font-family: "Noto Serif", Georgia, serif; }
  .panel { position: absolute; left: 40px; top: 138px; width: 1127px; height: 724px; background: var(--brand-orange); }
  .connectors { position: absolute; left: 0; top: 0; width: 1200px; height: 1000px; }
  .connectors path { stroke: var(--paper); stroke-width: 2; fill: none; }
  .title { position: absolute; left: 55px; top: 150px; font-size: 35px; font-style: italic; font-weight: 600; color: var(--paper); letter-spacing: -0.3px; }
  .column-head { position: absolute; top: 168px; font-size: 17px; font-weight: 600; color: var(--paper); transform: translateX(-50%); white-space: nowrap; }
  .node {
    position: absolute; background: var(--paper); color: var(--ink);
    display: flex; align-items: center; justify-content: center; text-align: center;
    font-style: italic; font-weight: 600; font-size: 16px; line-height: 1.1; white-space: nowrap;
  }
  .node--root { left: 72px; top: 417px; width: 173px; height: 107px; font-size: 17px; white-space: normal; }
  .node--process { left: 285px; width: 188px; height: 41px; font-size: 17px; }
  .node--driver { left: 520px; width: 285px; height: 31px; padding-left: 32px; padding-right: 4px; letter-spacing: -0.2px; }
  .node--sub { left: 867px; width: 282px; height: 29px; }
  .badge {
    position: absolute; left: 503px; width: 44px; height: 44px; border-radius: 50%;
    background: var(--brand-maroon); color: var(--paper); border: 2px solid var(--paper);
    display: flex; align-items: center; justify-content: center;
    font-style: italic; font-weight: 600; font-size: 27px;
  }
</style>
</head>
<body>
<div class="canvas">
  <div class="panel"></div>

  <svg class="connectors" viewBox="0 0 1200 1000" aria-hidden="true">
    <path d="M245 476 H263 M263 273 V705 M263 273 H285 M263 476 H285 M263 705 H285"/>
    <path d="M473 273 H495 M495 222 V323 M495 222 H505 M495 273 H505 M495 323 H505"/>
    <path d="M473 476 H495 M495 436 V536 M495 436 H505 M495 486 H505 M495 536 H505"/>
    <path d="M473 705 H495 M495 674 V775 M495 674 H505 M495 725 H505 M495 775 H505"/>
    <path d="M805 436 H835 M805 486 H835 M835 311 V486 M835 311 H867 M835 350 H867 M835 410 H867 M835 449 H867"/>
    <path d="M805 536 H835 M835 498 V576 M835 498 H867 M835 536 H867 M835 576 H867"/>
    <path d="M805 674 H835 M835 629 V707 M835 629 H867 M835 669 H867 M835 707 H867"/>
    <path d="M805 725 H835 M835 725 V834 M835 756 H867 M835 795 H867 M835 834 H867"/>
  </svg>

  <h1 class="title">Receivables</h1>
  <div class="column-head" style="left:374px">Sub-Process</div>
  <div class="column-head" style="left:667px">Drivers</div>
  <div class="column-head" style="left:1006px">Sub-Drivers</div>

  <div class="node node--root">Receivables<br>Drivers</div>

  <div class="node node--process" style="top:252px">Approval</div>
  <div class="node node--process" style="top:454px">Sales</div>
  <div class="node node--process" style="top:684px">Collections</div>

  <div class="node node--driver" style="top:207px">Differential terms</div>
  <div class="node node--driver" style="top:257px">Customer agreements</div>
  <div class="node node--driver" style="top:308px">Account set-up</div>
  <div class="node node--driver" style="top:420px">Receipt process</div>
  <div class="node node--driver" style="top:471px">Time to invoice</div>
  <div class="node node--driver" style="top:520px">Customer payment behaviour</div>
  <div class="node node--driver" style="top:659px">Payment cycle</div>
  <div class="node node--driver" style="top:710px">Collections</div>
  <div class="node node--driver" style="top:760px">Penalties</div>

  <div class="badge" style="top:200px">1</div>
  <div class="badge" style="top:251px">2</div>
  <div class="badge" style="top:301px">3</div>
  <div class="badge" style="top:414px">4</div>
  <div class="badge" style="top:464px">5</div>
  <div class="badge" style="top:514px">6</div>
  <div class="badge" style="top:652px">7</div>
  <div class="badge" style="top:703px">8</div>
  <div class="badge" style="top:753px">9</div>

  <div class="node node--sub" style="top:297px">Cash</div>
  <div class="node node--sub" style="top:336px">Banking process</div>
  <div class="node node--sub" style="top:396px">Sales delivery</div>
  <div class="node node--sub" style="top:434px">Invoicing</div>
  <div class="node node--sub" style="top:484px">KPI</div>
  <div class="node node--sub" style="top:522px">Relationship</div>
  <div class="node node--sub" style="top:562px">Pricing</div>
  <div class="node node--sub" style="top:615px">Closing date</div>
  <div class="node node--sub" style="top:654px">Time to process</div>
  <div class="node node--sub" style="top:693px">Invoicing cycle</div>
  <div class="node node--sub" style="top:742px">Tracking</div>
  <div class="node node--sub" style="top:781px">Methods</div>
  <div class="node node--sub" style="top:820px">Agencies</div>
</div>
</body>
</html>
```